Honey Label for a private beekeeper

I am an "amateur" beekeeper and like to promote and sell my honey. The target group is anyone who likes honey. Task: The label design should basically be an "eye-catcher" and express the high quality of the natural product honey. In the narrower sense, but which should form a unit in the design: The first part is the so-called guaranty; he connects with the glass and tears when first opening the lid. The lock should be about 2 inches wide and 8 inches long, and adorned by the words 'The best of the nature'. In brackets you always find the english translation of the german text for a better understanding. The second part is the product label. For this there are no shape specifications but max. height is 5cm and maximum is 12cm (for 500g jar), but the following must be included in the account: "Please use the following placeholders", "first name last name", "street house number", "post code city name ") as well as the words" 500g "," Best Before Date ", (" Best before "), behind or below please leave blank space for the stamp imprint of the date," Store dry, dark and protected from heat! dry, dark and protected from heat), And - most important - the text: "Finest bee honey" and in new line "from Cologne - Porz (from Cologne - Porz)" as well as the two varieties "Summer Blossom" or "Spring Blossom" ... in the future may be added more varieties. The company logo should be used in a single color, so that the customer can quickly identify the type of honey in the glass. For this purpose, the respective honeysuckle color, in whatever form, dominate the label or a certain area of ​​it. I have uploaded a few labels from the internet that appealed to me about their style, but it's definitely not about making just one copy of one of these labels. Please use the german text on the label, the translation is just for you. Please contact me in case of any further questions or problems with my explanation. I'm looking forward to your designs! As an 'amateur' I run a hobby-beekeeping and want to drive out my evening gown and summer turkey honey. The target group is anyone who likes honey. Task The Etiketten_Design to be designed should basically be an "eye-catcher", have a high recognition value and express the high quality of the natural product honey. In the narrower sense, two independent parts of the label are to be designed, but which should form a unit in the design: The first part is the so-called warranty; he connects the lid with the glass and tears when first opening the lid. The lock should be about 2 cm wide and 8 cm long, and adorned by the saying 'the best of nature'. The second part is the actual product label. For this there are no size and shape specifications, but the following contents must be considered: The data of the beekeeper (please use the following placeholders "first name last name", "street house number", "ZIP place name") and the information "500g", "At least Best before: "(behind or below, please leave white space for the stamp imprint of the date)," dry, dark and protect from heat! ", and - most importantly - the text: finest bee honey (new line) from Cologne - Porz as well the two denominations spring blossom or summer bloom (in the future may be added more varieties). The logo of the company should be used, but it can also be used on the freshly-baked seal (see appendix) Each type of honey (summer blossom and spring blossom) should be associated with a color, so that the customer can quickly identify which type of honey is in the glass. For this, the respective honeysuckle color, in whatever form, should dominate the label or a certain area of ​​it. With regard to a good reproducibility of the labels in large quantities, we ask for the following further requirements to be observed: • Please place text and picture elements with 4mm distance to the label edges. • Please consider the CYMK color scheme. • If you choose multicolored labels, please use a maximum of four colors. • The honeysuckle color of the product label should NOT be found on the warranty seal (because the guarantee applies generally to any honey jar, regardless of the honeys). • The product label should be editable. • The product label should be scalable (for both small 250g glasses and large 500g glasses). The last two points can be ignored if a larger copy with the indication "500g" and a smaller one with the indication "250g" are created per product label. I'm looking forward to your designs!

Target Market(s)

Neighborhood and shops

Colors

Designer to choose colors to be used in the design.

Requirements
Must have
• With regard to the following further requirements: • Please place text and picture elements 4mm from the edges of the labels. • Please consider the CYMK color scheme. • If you choose multicolored labels, please use a maximum of four colors. The honeysuckle color of the product label should not be found on the warranty. • The product label should be editable. • The product label needs to be scalable The "500g" and the smaller "250g" are created by product label.
Should not have
• Please do not use the color gold no transparent labels

```html
<!DOCTYPE html>
<html lang="de">
<head>
<meta charset="utf-8">
<title>Imkerei Lindner – Honey Label</title>
<link href="https://fonts.googleapis.com/css2?family=Lato:wght@700;900&family=Ultra&display=swap" rel="stylesheet">
<style>
  :root {
    --honey: #fdc116;
    --honey-mid: #fdd25a;
    --honey-light: #fde9a6;
    --ink: #060606;
    --slate: #2b2a35;
    --stage-dark: #3a3a3c;
    --stage-light: #a7a8ab;
    --white: #ffffff;
  }
  * { box-sizing: border-box; margin: 0; padding: 0; }
  html, body { width: 1200px; height: 1057px; overflow: hidden; }
  body {
    position: relative;
    background: linear-gradient(to bottom, var(--stage-dark) 0 746px, var(--stage-light) 746px 100%);
    font-family: "Lato", sans-serif;
  }

  /* Warranty seal */
  .seal {
    position: absolute; left: 546px; top: 69px; width: 108px; height: 425px;
    background: var(--honey);
    box-shadow: 2px 3px 6px rgba(0,0,0,.45);
    overflow: hidden;
  }
  .seal__motto {
    position: absolute; left: 54px; top: 245px;
    transform: translate(-50%, -50%) rotate(-90deg);
    white-space: nowrap;
    font-weight: 900; font-size: 31px; color: var(--slate);
  }
  .seal__tip { position: absolute; left: 0; bottom: 0; width: 108px; height: 25px; }

  /* Product label */
  .label {
    position: absolute; left: 118px; top: 546px; width: 964px; height: 402px;
    background: var(--honey);
    box-shadow: 2px 3px 6px rgba(0,0,0,.4);
    overflow: hidden;
  }
  .label__drip {
    position: absolute; top: 0; height: 240px;
    background: linear-gradient(to bottom, var(--honey-light) 0%, var(--honey-mid) 45%, var(--honey) 85%);
  }
  .label__drip--left { left: 0; width: 366px; }
  .label__drip--right { left: 597px; width: 367px; }

  .keeper {
    position: absolute; left: 27px; top: 32px; width: 137px; height: 340px;
    border: 2px solid rgba(255,236,170,.75); border-radius: 70px;
  }
  .keeper__text {
    position: absolute; left: 50%; top: 50%;
    transform: translate(-50%, -50%) rotate(-90deg);
    white-space: nowrap; color: var(--white); line-height: 1.05;
  }
  .keeper__title { font-weight: 900; font-size: 23px; }
  .keeper__address { font-weight: 700; font-size: 16px; margin-top: 4px; line-height: 1.1; }

  .weight {
    position: absolute; left: 196px; top: 350px; width: 118px;
    display: flex; align-items: center; gap: 6px;
    font-family: "Ultra", serif; font-size: 20px; color: var(--ink);
  }
  .weight::before, .weight::after { content: ""; flex: 1; height: 2px; background: var(--ink); }

  .brand-panel { position: absolute; left: 366px; top: 0; width: 231px; height: 260px; }
  .brand-panel svg { position: absolute; inset: 0; }
  .brand-panel__mark {
    position: absolute; left: 50%; top: 24px; width: 120px; height: 120px;
    transform: translateX(-50%); border-radius: 50%; background: var(--honey);
  }
  .brand-panel__name {
    position: absolute; left: 0; right: 0; top: 164px; text-align: center;
    font-weight: 900; font-size: 25px; line-height: 1.15; letter-spacing: 2px;
    color: var(--honey);
  }

  .product {
    position: absolute; left: 366px; width: 231px; text-align: center; color: var(--ink);
    font-family: "Ultra", serif; font-weight: 400; white-space: nowrap;
  }
  .product__sub { top: 260px; font-size: 21px; line-height: 1.2; }
  .product__name { top: 285px; font-size: 49px; line-height: 1.05; }

  .origin { position: absolute; left: 366px; top: 340px; width: 231px; height: 40px; }
  .origin svg { position: absolute; inset: 0; }
  .origin__text {
    position: absolute; left: 0; right: 0; top: 5px; text-align: center;
    font-family: "Ultra", serif; font-size: 12.5px; line-height: 1.25; color: var(--white);
    letter-spacing: .5px;
  }

  .storage {
    position: absolute; left: 680px; width: 245px; top: 230px; text-align: center;
    font-weight: 700; font-size: 17px; line-height: 1.22; color: var(--slate);
  }
  .best-before {
    position: absolute; left: 698px; top: 283px; width: 210px; height: 85px;
    background: var(--white); border-radius: 8px;
    text-align: center; padding-top: 8px;
    font-weight: 700; font-size: 16px; color: var(--slate);
  }
</style>
</head>
<body>

  <section class="seal" aria-label="Warranty seal">
    <p class="seal__motto">The Nest of the Nature</p>
    <svg class="seal__tip" viewBox="0 0 108 25" preserveAspectRatio="none" aria-hidden="true">
      <polygon points="0,12 54,0 108,12 108,25 0,25" fill="var(--ink)"/>
    </svg>
  </section>

  <section class="label" aria-label="Product label 500g">
    <div class="label__drip label__drip--left" role="img" aria-label="Illustration of golden honey dripping down from the top edge"></div>
    <div class="label__drip label__drip--right" role="img" aria-label="Illustration of golden honey dripping down from the top edge"></div>

    <div class="keeper">
      <div class="keeper__text">
        <p class="keeper__title">Finest bee honey<br>from Cologne - Porz</p>
        <p class="keeper__address">street house number<br>ZIP place name</p>
      </div>
    </div>

    <p class="weight">500g</p>

    <div class="brand-panel">
      <svg viewBox="0 0 231 260" preserveAspectRatio="none" aria-hidden="true">
        <polygon points="0,0 231,0 231,260 115.5,240 0,260" fill="var(--ink)"/>
      </svg>
      <span class="brand-panel__mark" aria-hidden="true"></span>
      <p class="brand-panel__name">IMKEREI<br>LINDNER</p>
    </div>

    <p class="product product__sub">Finest Bee</p>
    <h1 class="product product__name">HONEY</h1>

    <div class="origin">
      <svg viewBox="0 0 231 40" preserveAspectRatio="none" aria-hidden="true">
        <polygon points="0,10 115.5,0 231,10 231,40 0,40" fill="var(--ink)"/>
      </svg>
      <p class="origin__text">FROM<br>COLOGNE - PORZ</p>
    </div>

    <p class="storage">Dry, Dark And<br>Protected From Heat!</p>
    <div class="best-before">Best before:</div>
  </section>

</body>
</html>
```